Unique, Impressive, and Modern Business Card

Looking for a distinctive, unique business card. We are distributors of tire repairs supplies, tools, machinery, and chemicals. Our target market are tire repair shops, tire franchises, and mechanic shops. We would like our design to include tire characteristics, and use our business colors. Feel free to use all types design and printing options (emboss, spot uv, foil, etc) QR code may be applied, you can use different size business cards ( standard, square, rounded edge, colored edge, etc), all formats needed for printing, also editable for future changes

Target Market(s)

Automotive, Tire industries

Industry/Entity Type

Tire Industry (automotive)

Contact Information for Business Card

Business logo, business Name (Corvane Supply Inc), Name (Marcus Pellow), Position (President) Address (58 Fernhollow Lane, Brentwood NY 11742), Contact number (Company 1-855-302-4418, Cell 1-555-245-9073, email address (marcus.pellow@corvanesupply.com), URL (www.corvanesupply.com

Requirements
Must have
• Must include Business Colors (Black, Green, Blue, White) see sample website file
Nice to have
• emboss, spot uv, etc

```html
<!DOCTYPE html>
<html lang="en">
<head>
<meta charset="utf-8">
<title>Corvane Supply Business Card</title>
<link rel="stylesheet" href="https://fonts.googleapis.com/css2?family=Montserrat:wght@400;500;600&display=swap">
<style>
  :root {
    --stage: #c5c6c8;
    --ink: #161616;
    --green: #47b649;
    --green-deep: #34943a;
    --green-tread: #2f8a33;
    --blue: #344da1;
    --blue-deep: #243a86;
    --blue-tread: #26397f;
    --white: #ffffff;
    --edge-grey: #d9dadc;
  }
  html, body {
    margin: 0;
    padding: 0;
    width: 1200px;
    height: 1000px;
    overflow: hidden;
    background: var(--stage);
    font-family: "Montserrat", Arial, sans-serif;
  }
  .card {
    position: absolute;
    left: 272px;
    width: 657px;
    height: 425px;
    box-shadow: 0 2px 6px rgba(0, 0, 0, 0.25);
    display: block;
  }
  .card-front { top: 56px; }
  .card-back  { top: 519px; }
  .card text { font-family: "Montserrat", Arial, sans-serif; }
  .brand-name { fill: var(--white); font-weight: 500; }
  .person-name { fill: var(--white); font-weight: 600; }
  .person-role, .contact-line { fill: var(--white); font-weight: 400; }
  .icon-box { fill: var(--green); }
  .icon-glyph { fill: none; stroke: var(--white); stroke-width: 1.4; stroke-linecap: round; stroke-linejoin: round; }
  .icon-solid { fill: var(--white); }
</style>
</head>
<body>

<!-- Front side -->
<svg class="card card-front" viewBox="0 0 493 319" xmlns="http://www.w3.org/2000/svg">
  <rect class="front-base" width="493" height="319" fill="var(--ink)"/>
  <polygon class="front-green-panel" points="261,0 493,0 493,58 352,196" fill="var(--green)"/>
  <polygon class="front-green-edge" points="261,0 273,0 358,184 352,196" fill="var(--green-deep)"/>
  <polygon class="front-tread-green" role="img" aria-label="Tyre tread track texture" points="356,136 478,3 493,3 493,20 370,150" fill="var(--green-tread)" opacity="0.75"/>
  <polygon class="front-white-band" points="352,196 493,58 493,88 358,202" fill="var(--white)"/>
  <polygon class="front-grey-edge" points="358,202 493,88 493,96 362,206" fill="var(--edge-grey)"/>
  <polygon class="front-blue-panel" points="362,206 493,96 493,319 218,319" fill="var(--blue)"/>
  <polygon class="front-tread-blue" role="img" aria-label="Tyre tread track texture" points="221,319 412,160 432,166 252,319" fill="var(--blue-tread)" opacity="0.85"/>

  <circle class="brand-dot" cx="64" cy="162" r="38" fill="var(--white)"/>
  <text class="brand-name" x="110" y="170" font-size="22">Corvane Supply</text>
</svg>

<!-- Back side -->
<svg class="card card-back" viewBox="0 0 493 319" xmlns="http://www.w3.org/2000/svg">
  <rect class="back-base" width="493" height="319" fill="var(--ink)"/>
  <polygon class="back-white-corner" points="0,0 146,0 100,100 0,8" fill="var(--white)"/>
  <polygon class="back-grey-edge" points="0,8 100,100 98,106 0,16" fill="var(--edge-grey)"/>
  <polygon class="back-green-stripe" points="0,16 98,106 88,132 0,48" fill="var(--green)"/>
  <polygon class="back-blue-panel" points="146,0 493,0 493,319 286,319 88,132" fill="var(--blue)"/>
  <polygon class="back-blue-edge" points="88,132 286,319 274,319 86,138" fill="var(--blue-deep)"/>
  <polygon class="back-tread-blue" role="img" aria-label="Tyre tread track texture" points="166,0 200,0 130,96 112,96" fill="var(--blue-tread)" opacity="0.85"/>

  <text class="person-name" x="472" y="62" font-size="22" text-anchor="end">Marcus Pellow</text>
  <text class="person-role" x="472" y="83" font-size="15" text-anchor="end">President</text>

  <text class="contact-line" x="442" y="134" font-size="15" text-anchor="end">1-855-302-4418</text>
  <text class="contact-line" x="442" y="154" font-size="15" text-anchor="end">1-555-245-9073</text>
  <g class="icon icon-phone" transform="translate(453,120)">
    <rect class="icon-box" width="19" height="19"/>
    <path class="icon-solid" d="M5.5 4.5 L8 4.5 L9 7.5 L7.5 8.7 Q9 11.5 10.8 12 L12 10.5 L15 11.5 L15 14 Q14 15 12.5 15 Q5 13.5 4.5 6 Q4.5 4.8 5.5 4.5 Z"/>
  </g>

  <text class="contact-line" x="442" y="186" font-size="14.5" text-anchor="end">marcus.pellow@corvanesupply.com</text>
  <g class="icon icon-mail" transform="translate(453,172)">
    <rect class="icon-box" width="19" height="19"/>
    <rect class="icon-solid" x="4" y="5.5" width="11" height="8"/>
    <path d="M4.5 6 L9.5 10 L14.5 6" fill="none" stroke="var(--green)" stroke-width="1.2"/>
  </g>

  <text class="contact-line" x="442" y="218" font-size="15" text-anchor="end">58 Fernhollow Lane,</text>
  <text class="contact-line" x="442" y="238" font-size="15" text-anchor="end">Ashcombe OH 43719</text>
  <g class="icon icon-pin" transform="translate(453,205)">
    <rect class="icon-box" width="19" height="19"/>
    <path class="icon-solid" d="M9.5 16 Q5 10.5 5 8 A4.5 4.5 0 0 1 14 8 Q14 10.5 9.5 16 Z"/>
    <circle cx="9.5" cy="8" r="1.7" fill="var(--green)"/>
  </g>

  <text class="contact-line" x="442" y="270" font-size="15" text-anchor="end">www.corvanesupply.com</text>
  <g class="icon icon-web" transform="translate(453,257)">
    <rect class="icon-box" width="19" height="19"/>
    <circle class="icon-glyph" cx="9.5" cy="9.5" r="5.5"/>
    <ellipse class="icon-glyph" cx="9.5" cy="9.5" rx="2.4" ry="5.5"/>
    <line class="icon-glyph" x1="4" y1="9.5" x2="15" y2="9.5"/>
  </g>

  <circle class="brand-dot" cx="44" cy="272" r="24" fill="var(--white)"/>
  <text class="brand-name" x="76" y="269" font-size="11">Corvane</text>
  <text class="brand-name" x="76" y="283" font-size="11">Supply Inc</text>
</svg>

</body>
</html>
```